Velvet Lantern rebranding my business with a new business card

I have my new logo and now I need a refresher on my business cards. I really want something fun and fresh. I like black background or anything to make the color pop.
Logo
Name: Velvet Lantern
Contact Info as stated below:
Mara Pelkin
519-555-0147
Logo
Name: Velvet Lantern
Mara Pelkin
519-555-0147
fb.me/VelvetLanternbyMara
Instagram: @VelvetLanternbyMara

Industry/Entity Type

Business

Contact Information for Business Card

double-sided. Logo on one side. Contact info on the other.

Requirements
Must have
• Logo
• Name: Velvet Lantern
• Contact Info as stated below:
• Mara Pelkin
• 519-555-0147
• fb.me/VelvetLanternbyMara
• fb.me/VelvetLanternbyMara

```html
<!DOCTYPE html>
<html lang="en">
<head>
<meta charset="utf-8">
<title>Velvet Lantern – Business Card</title>
<link href="https://fonts.googleapis.com/css2?family=Cormorant+Garamond:ital,wght@1,600&family=Open+Sans:wght@400;600&display=swap" rel="stylesheet">
<style>
  :root {
    --page: #e9e4de;
    --card-black: #111013;
    --card-pattern: #1c1a20;
    --band-pink: #d23cb4;
    --band-pink-soft: #e170cc;
    --text-light: #f4f0f2;
    --text-muted: #cfc6cc;
    --logo-lilac: #e6bfe8;
  }
  * { margin: 0; padding: 0; box-sizing: border-box; }
  html, body {
    width: 1200px; height: 1023px; overflow: hidden;
    background: var(--page);
    font-family: "Open Sans", sans-serif;
  }
  .sheet {
    width: 1200px; height: 1023px;
    display: flex; flex-direction: column; align-items: center; justify-content: center;
    gap: 60px;
  }
  .card {
    position: relative;
    width: 720px; height: 411px;
    background: radial-gradient(ellipse at 50% 50%, var(--card-pattern), var(--card-black) 75%);
    box-shadow: 0 6px 18px rgba(0,0,0,.25);
    overflow: hidden;
  }
  .band {
    position: absolute; left: 0; right: 0; height: 42px;
    background: linear-gradient(var(--band-pink-soft), var(--band-pink));
  }
  .band--top { top: 0; }
  .band--bottom { bottom: 0; }

  /* front */
  .identity {
    position: absolute; top: 70px; right: 52px; text-align: right;
  }
  .identity__name {
    font-family: "Cormorant Garamond", serif; font-style: italic; font-weight: 600;
    font-size: 44px; color: var(--text-light); line-height: 1;
  }
  .identity__title {
    font-size: 17px; color: var(--text-muted); margin-top: 4px;
  }
  .contacts {
    position: absolute; top: 172px; right: 52px; list-style: none; text-align: right;
  }
  .contacts li {
    font-size: 19px; color: var(--text-light); line-height: 32px;
    display: flex; justify-content: flex-end; align-items: center; gap: 12px;
  }
  .contacts .icon-slot { width: 16px; height: 16px; display: inline-flex; }
  .brand-block {
    position: absolute; left: 44px; bottom: 64px;
  }
  .brand-art {
    width: 200px; height: 120px; margin-bottom: 14px;
    display: flex; align-items: center; gap: 12px;
  }
  .brand-dot {
    width: 28px; height: 28px; border-radius: 50%; background: var(--logo-lilac);
  }
  .brand-wordmark {
    font-size: 24px; font-weight: 600; color: var(--logo-lilac);
  }
  .address { font-size: 19px; color: var(--text-light); line-height: 26px; }

  /* back */
  .emblem {
    position: absolute; left: 50%; top: 50%; transform: translate(-50%, -50%);
    width: 236px; height: 236px; border-radius: 50%;
    border: 3px solid var(--logo-lilac);
    display: flex; align-items: center; justify-content: center;
  }
  .emblem .brand-wordmark { font-size: 26px; text-align: center; line-height: 1.2; }
</style>
</head>
<body>
<main class="sheet">
  <section class="card card--front" aria-label="Card front">
    <div class="band band--top"></div>
    <div class="identity">
      <div class="identity__name">Mara Pelkin</div>
      <div class="identity__title">Your Title</div>
    </div>
    <ul class="contacts">
      <li>519-555-0147
        <span class="icon-slot">
          <svg viewBox="0 0 16 16" width="16" height="16" aria-hidden="true"><path d="M4 1.5l2.5 3-1.3 1.6a8 8 0 0 0 4.7 4.7l1.6-1.3 3 2.5-1.6 2.2C7.8 14 2 8.2 1.8 3.1z" fill="#f4f0f2"/></svg>
        </span>
      </li>
      <li>fb.me/VelvetLanternbyMara <span class="icon-slot"></span></li>
      <li>VelvetLanternbyMara <span class="icon-slot"></span></li>
    </ul>
    <div class="brand-block">
      <div class="brand-art">
        <span class="brand-dot"></span>
        <span class="brand-wordmark">Velvet Lantern</span>
      </div>
      <div class="address">Velvet Lantern<br>Harlow Creek, Ontario N0J4X2</div>
    </div>
    <div class="band band--bottom"></div>
  </section>

  <section class="card card--back" aria-label="Card back">
    <div class="band band--top"></div>
    <div class="emblem">
      <span class="brand-wordmark">Velvet<br>Lantern</span>
    </div>
    <div class="band band--bottom"></div>
  </section>
</main>
</body>
</html>
```